Business Card Design

Quorvel Software Limited develops and sells venue and event management software called Quorvel Stagehand, which is available in the cloud or on-premise. The company was established in 1986. Most of our customers are performing arts venues, museums and festivals. Our existing design is a bit dull. We need to convey that we are both innovative and reliable.
Not all our people show their mobile phone numbers on their cards, so the design needs to work land line and mobile or land line only.

Industry/Entity Type

Software

Contact Information for Business Card

Helen Trasko
Director
Quorvel Software Limited
42B Milbrook Lane, Epsom, Surrey, KT19 4DN
Telephone: +44 (0)1372 640913
Mobile: +44 (0)7945 216804
Email: htrasko@quorvel.net
Web: www.quorvel.net

```html
<!DOCTYPE html>
<html lang="en">
<head>
<meta charset="utf-8">
<title>Quorvel Software Limited — Business Card</title>
<link rel="stylesheet" href="https://fonts.googleapis.com/css2?family=Open+Sans:wght@400;600;700&display=swap">
<style>
  :root {
    --backdrop: #e6e7e9;
    --card: #ffffff;
    --navy: #1f3b5e;
    --blue: #4a7bab;
    --rule: #9dbad6;
    --ink: #3c4248;
    --shadow: rgba(20, 30, 45, 0.18);
  }
  * { margin: 0; padding: 0; box-sizing: border-box; }
  html, body {
    width: 1200px; height: 913px; overflow: hidden;
    background: var(--backdrop);
    font-family: "Open Sans", Arial, sans-serif;
  }
  .canvas { position: relative; width: 1200px; height: 913px; }
  .card {
    position: absolute; width: 525px; height: 300px;
    background: var(--card);
    box-shadow: 0 6px 18px var(--shadow);
  }
  .card--front { left: 70px; top: 130px; }
  .card--back { left: 605px; top: 480px; }

  .wordmark {
    position: absolute; display: flex; align-items: center; gap: 14px;
    color: var(--navy); font-weight: 700; white-space: nowrap;
  }
  .wordmark__square { width: 34px; height: 34px; background: var(--blue); flex: none; }
  .card--front .wordmark {
    left: 50%; top: 50%; transform: translate(-50%, -50%);
    font-size: 46px; letter-spacing: 0.04em;
  }
  .card--front .wordmark__square { width: 44px; height: 44px; }

  .card--back .wordmark { left: 38px; top: 52px; gap: 12px; }
  .card--back .wordmark__square { width: 40px; height: 40px; }
  .wordmark__text { display: flex; flex-direction: column; line-height: 1.05; }
  .wordmark__name { font-size: 25px; letter-spacing: 0.04em; }
  .wordmark__legal { font-size: 13.5px; letter-spacing: 0.01em; }

  .person { position: absolute; left: 110px; top: 178px; text-align: right; }
  .person__name { color: var(--navy); font-weight: 700; font-size: 16px; line-height: 1.2; }
  .person__role { color: var(--blue); font-size: 10.5px; }

  .contact { position: absolute; left: 286px; top: 48px; width: 222px; }
  .contact__list { list-style: none; }
  .contact__item {
    display: flex; align-items: center; gap: 10px;
    font-size: 10.5px; color: var(--ink); line-height: 18px; white-space: nowrap;
  }
  .contact__icon { width: 12px; height: 12px; flex: none; fill: var(--ink); }
  .contact__rule { height: 1px; background: var(--rule); margin: 8px 0 7px; }
  .contact__address { font-size: 9.5px; color: var(--ink); white-space: nowrap; }
</style>
</head>
<body>
<main class="canvas">
  <section class="card card--front" aria-label="Card front">
    <div class="wordmark"><span class="wordmark__square"></span>QUORVEL</div>
  </section>

  <section class="card card--back" aria-label="Card back">
    <div class="wordmark">
      <span class="wordmark__square"></span>
      <span class="wordmark__text">
        <span class="wordmark__name">QUORVEL</span>
        <span class="wordmark__legal">Software Limited</span>
      </span>
    </div>

    <div class="person">
      <p class="person__name">Helen Trasko</p>
      <p class="person__role">Director</p>
    </div>

    <div class="contact">
      <ul class="contact__list">
        <li class="contact__item">
          <svg class="contact__icon" viewBox="0 0 12 12" aria-hidden="true"><path d="M2 1h2.5l1 3-1.5 1a6 6 0 0 0 3 3l1-1.5 3 1V10a1 1 0 0 1-1 1A9 9 0 0 1 1 2a1 1 0 0 1 1-1z"/></svg>
          +44 (0)1372 640913
        </li>
        <li class="contact__item">
          <svg class="contact__icon" viewBox="0 0 12 12" aria-hidden="true"><path d="M3 0h6a1 1 0 0 1 1 1v10a1 1 0 0 1-1 1H3a1 1 0 0 1-1-1V1a1 1 0 0 1 1-1zm0 2v7h6V2z"/></svg>
          +44 (0)7945 216804
        </li>
        <li class="contact__item">
          <svg class="contact__icon" viewBox="0 0 12 12" aria-hidden="true"><path d="M0 2h12v8H0zm1 1v.3l5 3.2 5-3.2V3zm0 1.5V9h10V4.5L6 7.7z"/></svg>
          htrasko@quorvel.net
        </li>
        <li class="contact__item">
          <svg class="contact__icon" viewBox="0 0 12 12" aria-hidden="true"><path d="M6 0a6 6 0 1 0 0 12A6 6 0 0 0 6 0zm0 1c.8 0 1.6 1.7 1.8 4.5H4.2C4.4 2.7 5.2 1 6 1zM1 6.5h2.2c.1 1.8.4 3.3 1 4.2A5 5 0 0 1 1 6.5zm0-1a5 5 0 0 1 3.2-4.2c-.6.9-.9 2.4-1 4.2zm5 5.5c-.8 0-1.6-1.7-1.8-4.5h3.6C7.6 9.3 6.8 11 6 11zm1.8-.3c.6-.9.9-2.4 1-4.2H11a5 5 0 0 1-3.2 4.2zM8.8 5.5c-.1-1.8-.4-3.3-1-4.2A5 5 0 0 1 11 5.5z"/></svg>
          www.quorvel.net
        </li>
      </ul>
      <div class="contact__rule"></div>
      <p class="contact__address">42B Milbrook Lane, Epsom, Surrey, KT19 4DN</p>
    </div>
  </section>
</main>
</body>
</html>
```